Icons für Entwickler von Onlinetools, Onlinekonfiguratoren
Zielgruppe
Wir entwickeln Onlinetools, Onlinekonfiguratoren für die Gewerke Sanitär, Heizung, Klima und Lüftung und darüber hinaus für Elektro, Dachdecker und Zimmerer.
Aufgabenstellung
Wir benötigen für die Weiterentwicklung eines vorhandenen Onlinetools (Photovoltaik-Rechner) ca. 40 zusätzliche Icons. Diese sollten sich an den vorhandenen Icons anlehnen. Als Format benötigen wir SVG.

```html
<!DOCTYPE html>
<html lang="de">
<head>
<meta charset="utf-8">
<title>Photovoltaik-Rechner Icons</title>
<link rel="stylesheet" href="https://fonts.googleapis.com/css2?family=Source+Sans+3:wght@400&display=swap">
<style>
  :root {
    --tile-active: #666666;
    --tile-yellow: #F6BE1C;
    --icon: #ffffff;
    --ink: #000000;
    --paper: #ffffff;
  }
  html, body { margin: 0; padding: 0; overflow: hidden; }
  body { width: 692px; height: 1200px; background: var(--paper); position: relative;
         font-family: "Source Sans 3", "Myriad Pro", sans-serif; }
  .section-title { position: absolute; left: 0; width: 692px; margin: 0; text-align: center;
                   font-weight: 400; font-size: 47px; line-height: 1; color: var(--ink); }
  .tile { position: absolute; width: 154px; height: 140px; display: block; }
  .tile svg { width: 100%; height: 100%; display: block; }
  .tile-label { font-family: "Source Sans 3", "Myriad Pro", sans-serif; font-size: 29px;
                fill: var(--icon); text-anchor: middle; }
  .is-selected { background: var(--tile-active); }
  .is-option { background: var(--tile-yellow); }
  .stroke { stroke: var(--icon); stroke-width: 5; fill: none; }
  .fill { fill: var(--icon); }
</style>
</head>
<body>

<h1 class="section-title" style="top:37px">Anzal Etagen</h1>

<div class="tile is-selected" style="left:70px; top:112px">
  <svg viewBox="0 0 325 295">
    <polygon class="fill" points="117,120 163,91 208,120"/>
    <rect class="fill" x="117" y="127" width="91" height="33"/>
    <text class="tile-label" x="163" y="205">1</text>
  </svg>
</div>
<div class="tile is-option" style="left:269px; top:112px">
  <svg viewBox="0 0 325 295">
    <polygon class="fill" points="117,102 162,73 207,102"/>
    <rect class="fill" x="117" y="106" width="90" height="36"/>
    <rect class="fill" x="117" y="148" width="90" height="33"/>
    <text class="tile-label" x="162" y="222">2</text>
  </svg>
</div>
<div class="tile is-option" style="left:467px; top:112px">
  <svg viewBox="0 0 325 295">
    <polygon class="fill" points="117,81 163,52 208,81"/>
    <rect class="fill" x="117" y="88" width="91" height="33"/>
    <rect class="fill" x="117" y="127" width="91" height="33"/>
    <rect class="fill" x="117" y="166" width="91" height="34"/>
    <text class="tile-label" x="163" y="243">3</text>
  </svg>
</div>

<h1 class="section-title" style="top:377px">Dachneigung</h1>

<div class="tile is-selected" style="left:70px; top:456px">
  <svg viewBox="0 0 325 295">
    <line class="stroke" x1="117" y1="147" x2="208" y2="147"/>
    <text class="tile-label" x="163" y="192">0°</text>
  </svg>
</div>
<div class="tile is-option" style="left:269px; top:456px">
  <svg viewBox="0 0 325 295">
    <polyline class="stroke" points="203,131 121,147 203,147"/>
    <text class="tile-label" x="165" y="192">10°</text>
  </svg>
</div>
<div class="tile is-option" style="left:467px; top:456px">
  <svg viewBox="0 0 325 295">
    <polyline class="stroke" points="200,118 121,148 204,148"/>
    <text class="tile-label" x="163" y="193">20°</text>
  </svg>
</div>
<div class="tile is-option" style="left:70px; top:637px">
  <svg viewBox="0 0 325 295">
    <polyline class="stroke" points="194,105 121,147 204,147"/>
    <text class="tile-label" x="165" y="195">30°</text>
  </svg>
</div>
<div class="tile is-option" style="left:269px; top:637px">
  <svg viewBox="0 0 325 295">
    <polyline class="stroke" points="185,94 121,147 204,147"/>
    <text class="tile-label" x="166" y="195">40°</text>
  </svg>
</div>
<div class="tile is-option" style="left:467px; top:637px">
  <svg viewBox="0 0 325 295">
    <polyline class="stroke" points="176,83 121,147 204,147"/>
    <text class="tile-label" x="165" y="196">50°</text>
  </svg>
</div>

<h1 class="section-title" style="top:902px; left:10px">Zubehör</h1>

<div class="tile is-selected" style="left:66px; top:985px">
  <svg viewBox="0 0 325 295">
    <circle class="stroke" cx="163" cy="140" r="43" stroke-width="4"/>
    <rect class="fill" x="136" y="120" width="54" height="38" rx="9"/>
    <rect class="fill" x="146" y="155" width="6" height="12"/>
    <rect class="fill" x="158" y="155" width="6" height="12"/>
    <path class="stroke" d="M135,165 q8,10 20,12" stroke-width="6"/>
    <circle class="fill" cx="151" cy="177" r="8"/>
    <text class="tile-label" x="162" y="226">Wallbox</text>
  </svg>
</div>
<div class="tile is-option" style="left:265px; top:985px">
  <svg viewBox="0 0 325 295">
    <polygon class="fill" points="132,95 148,95 145,113 127,113"/>
    <polygon class="fill" points="152,95 168,95 168,113 150,113"/>
    <polygon class="fill" points="172,95 188,95 192,113 173,113"/>
    <polygon class="fill" points="126,117 145,117 142,137 120,137"/>
    <polygon class="fill" points="150,117 168,117 168,137 148,137"/>
    <polygon class="fill" points="173,117 193,117 199,137 175,137"/>
    <polygon class="fill" points="119,141 141,141 138,164 112,164"/>
    <polygon class="fill" points="148,141 168,141 168,164 146,164"/>
    <polygon class="fill" points="175,141 200,141 208,164 177,164"/>
    <rect class="fill" x="153" y="166" width="16" height="20" rx="3"/>
    <text class="tile-label" x="162" y="226">Kollektor</text>
  </svg>
</div>
<div class="tile is-option" style="left:464px; top:985px">
  <svg viewBox="0 0 325 295">
    <path class="stroke" d="M116,132 A44,44 0 0 1 203,132" stroke-width="4"/>
    <path class="stroke" d="M116,148 A44,44 0 0 0 203,148" stroke-width="4"/>
    <line class="stroke" x1="114" y1="140" x2="128" y2="140" stroke-width="4"/>
    <line class="stroke" x1="191" y1="140" x2="205" y2="140" stroke-width="4"/>
    <path class="fill" d="M128,140 l10,-9 h8 v18 h-8 z"/>
    <rect class="fill" x="148" y="128" width="6" height="24"/>
    <rect class="fill" x="164" y="128" width="7" height="24"/>
    <path class="fill" d="M173,130 h6 q12,0 12,10 q0,10 -12,10 h-6 z"/>
    <text class="tile-label" x="160" y="226">Anschluss</text>
  </svg>
</div>

</body>
</html>
```